Email Notification & Marketing Templates

I want to start with something like a newsletter or informational email, but i need Top Tips to Detect Phishing Scams. Something that i can send to users so they can follow it when receiving or exchanging emails. I will also need promotional items for my company that i can send to customers as well. It can be based on on our website PLVORIX.COM

Will also need:
newsletters
announcements
marketing emails
alerts
security notifications

Examples:Items such as Security Awareness Poster Series
Phishing Awareness
Password Security
Email Attachments
QR Code scams
Public WiFi safety

```html
<!DOCTYPE html>
<html lang="en">
<head>
<meta charset="utf-8">
<title>Plvorix – IT Services Flyer</title>
<link rel="stylesheet" href="https://fonts.googleapis.com/css2?family=Outfit:wght@400;500;600;700&family=Playfair+Display:ital,wght@1,700&display=swap">
<style>
:root{
  --green:#1f8a14;
  --green-dark:#17700f;
  --mint:#dfe9cf;
  --mint-soft:#eef5e4;
  --ink:#1c1c1c;
  --grey:#9a9a9a;
  --stage:#232323;
  --paper:#ffffff;
}
*{margin:0;padding:0;box-sizing:border-box}
html,body{width:1011px;height:1200px;overflow:hidden;background:var(--stage)}
body{font-family:"Outfit",sans-serif;color:var(--ink)}
.flyer{position:absolute;left:105px;top:0;width:800px;height:1200px;background:var(--paper);overflow:hidden}
.backdrop{position:absolute;left:0;top:0}
.brand{position:absolute;right:28px;top:20px;display:flex;align-items:center;gap:10px}
.brand-name{font-size:50px;font-weight:700;color:var(--green);letter-spacing:1px;line-height:1}
.brand-mark{width:26px;height:26px;background:var(--green)}
.headline{position:absolute;right:26px;top:268px;text-align:right;font-size:49px;line-height:58px}
.headline .strong{font-weight:700;color:var(--green)}
.headline .soft{font-weight:400;color:var(--ink)}
.head-rule{position:absolute;left:690px;top:517px;width:69px;height:3px;background:var(--green)}
.tagline{position:absolute;left:570px;top:568px;width:230px;text-align:center;font-family:"Playfair Display",serif;font-style:italic;font-weight:700;font-size:22px;line-height:30px;color:var(--green)}
.section-band{position:absolute;left:257px;top:680px;width:288px;height:43px}
.section-title{position:absolute;left:257px;top:680px;width:288px;line-height:43px;text-align:center;font-size:24px;font-weight:700;color:var(--green)}
.service{position:absolute;top:757px;width:250px;text-align:center}
.service-icon{display:block;margin:0 auto;width:56px;height:52px;border:1.5px solid var(--green);border-radius:5px}
.service-title{margin-top:12px;font-size:20px;font-weight:700;color:var(--green);letter-spacing:.3px}
.service-text{margin-top:6px;font-size:14.5px;line-height:25px;color:var(--ink)}
.divider{position:absolute;top:760px;width:1px;height:175px;background:#8a8a8a}
.about-title{position:absolute;left:33px;top:988px;font-size:25px;font-weight:700;color:var(--green)}
.rule{position:absolute;height:3px;width:52px;background:var(--grey)}
.about-text{position:absolute;left:36px;top:1046px;width:330px;font-size:14.5px;line-height:25px}
.motto{position:absolute;left:35px;top:1190px}
.motto .big{display:block;font-size:44px;font-weight:600;color:var(--green);line-height:48px;letter-spacing:.5px}
.motto .sub{display:block;font-size:33px;font-weight:600;color:#2a2a2a;line-height:44px}
.contact-title{position:absolute;left:505px;top:1033px;font-size:25px;font-weight:700;color:var(--green)}
.contact-list{position:absolute;left:513px;top:1100px;list-style:none;font-size:14.5px}
.contact-list li{display:flex;align-items:flex-start;gap:6px;margin-bottom:18px;line-height:17px}
.contact-list svg{flex:none;width:22px;height:22px;margin-top:-3px}
.footer-band{position:absolute;left:0;bottom:0;width:800px;height:20px;background:linear-gradient(90deg,#e6efd8,#eaf5dc)}
</style>
</head>
<body>
<main class="flyer">
  <svg class="backdrop" width="800" height="1200" viewBox="0 0 800 1200">
    <defs>
      <linearGradient id="mintFade" x1="0" y1="0" x2="1" y2="1">
        <stop offset="0" stop-color="#d9e5c9"/><stop offset="1" stop-color="#e6efda"/>
      </linearGradient>
      <linearGradient id="photoTone" x1="0" y1="0" x2="1" y2="1">
        <stop offset="0" stop-color="#1d3550"/><stop offset=".55" stop-color="#2c4a68"/><stop offset="1" stop-color="#c9d3dc"/>
      </linearGradient>
      <linearGradient id="silver" x1="0" y1="0" x2="1" y2="0">
        <stop offset="0" stop-color="#c9c9c9"/><stop offset=".5" stop-color="#eeeeee"/><stop offset="1" stop-color="#dedede"/>
      </linearGradient>
      <linearGradient id="streak" x1="0" y1="0" x2="1" y2="1">
        <stop offset="0" stop-color="#d6d6d6"/><stop offset="1" stop-color="#ffffff" stop-opacity="0"/>
      </linearGradient>
      <linearGradient id="contactFade" x1="0" y1="0" x2="1" y2="1">
        <stop offset="0" stop-color="#f4f8ee"/><stop offset="1" stop-color="#e3f0cf"/>
      </linearGradient>
    </defs>
    <polygon points="0,0 466,0 376,195 0,195" fill="url(#mintFade)"/>
    <polygon points="0,195 376,195 345,262 0,262" fill="url(#mintFade)"/>
    <polygon points="0,262 0,542 201,542 0,222" fill="url(#mintFade)"/>
    <polygon points="0,162 348,162 576,540 196,540 0,220" fill="#ffffff"/>
    <polygon role="img" aria-label="Photo of an IT technician working at a monitor showing a network diagram" points="0,174 338,174 560,534 212,534 0,235" fill="url(#photoTone)"/>
    <polygon points="718,548 746,548 818,662 790,662" fill="url(#streak)"/>
    <polygon class="section-band" points="282,680 545,680 520,723 257,723" fill="url(#silver)"/>
    <polygon points="376,1012 800,1012 800,1180 547,1180" fill="url(#contactFade)"/>
    <polygon points="627,1170 652,1170 565,1028 540,1028" fill="url(#streak)" opacity=".7"/>
  </svg>

  <div class="brand"><span class="brand-mark"></span><span class="brand-name">PLVORIX</span></div>

  <h1 class="headline">
    <span class="strong">More Than IT<br>Support.</span><br>
    <span class="soft">We're Your IT<br>Partner.</span>
  </h1>
  <div class="head-rule"></div>
  <p class="tagline">Built for Business of<br>All Sizes.<br>Especially Yours.</p>

  <h2 class="section-title">OUR SERVICES</h2>

  <section class="service" style="left:11px">
    <svg class="service-icon" viewBox="0 0 56 52"><rect x="20" y="22" width="16" height="13" rx="2" fill="var(--green)"/><path d="M23 22v-4a5 5 0 0 1 10 0v4" fill="none" stroke="var(--green)" stroke-width="2"/></svg>
    <h3 class="service-title">CYBERSECURITY</h3>
    <p class="service-text">Protect your business from online threats with our comprehensive and cutting-edge cybersecurity solutions.</p>
  </section>
  <div class="divider" style="left:270px"></div>
  <section class="service" style="left:275px;top:760px">
    <svg class="service-icon" viewBox="0 0 56 52"><circle cx="30" cy="20" r="7" fill="none" stroke="var(--green)" stroke-width="4"/><path d="M12 40h22l10-6" fill="none" stroke="var(--green)" stroke-width="3"/></svg>
    <h3 class="service-title">MANAGED SERVICES</h3>
    <p class="service-text">Keep your business running smoothly with proactive and personalized tech management.</p>
  </section>
  <div class="divider" style="left:531px"></div>
  <section class="service" style="left:531px">
    <svg class="service-icon" viewBox="0 0 56 52"><circle cx="28" cy="26" r="13" fill="var(--green)"/><circle cx="28" cy="26" r="7" fill="#fff"/></svg>
    <h3 class="service-title">IT CONSULTING</h3>
    <p class="service-text">Transform your tech strategy with expert guidance tailored to your unique business goals.</p>
  </section>

  <h2 class="about-title">WHO WE ARE</h2>
  <div class="rule" style="left:35px;top:1026px"></div>
  <p class="about-text">At Plvorix, we're passionate about infusing a personal touch into IT services. Serving the Riverton area, our mission is to provide prompt, reliable, and affordable IT management and support to businesses of all sizes.</p>
  <p class="motto"><span class="big">PERSONAL TOUCH</span><span class="sub">PROFESSIONAL SERVICE</span></p>

  <h2 class="contact-title">CONTACT US</h2>
  <div class="rule" style="left:508px;top:1073px"></div>
  <ul class="contact-list">
    <li><svg viewBox="0 0 22 22"><rect x="4" y="4" width="14" height="14" transform="rotate(45 11 11)" fill="var(--green)"/><path d="M8 7l2 2-1 1 3 3 1-1 2 2-2 1c-3 0-6-3-6-6z" fill="#fff"/></svg><strong>(555) 014-3201</strong></li>
    <li><svg viewBox="0 0 22 22"><rect x="4" y="4" width="14" height="14" transform="rotate(45 11 11)" fill="var(--green)"/><rect x="7" y="8" width="8" height="6" fill="#fff"/><path d="M7 8l4 3 4-3" fill="none" stroke="var(--green)"/></svg>info@plvorix.com</li>
    <li><svg viewBox="0 0 22 22"><rect x="4" y="4" width="14" height="14" transform="rotate(45 11 11)" fill="var(--green)"/><circle cx="11" cy="11" r="4" fill="none" stroke="#fff" stroke-width="1.3"/><path d="M7 11h8M11 7v8" stroke="#fff" stroke-width="1"/></svg>plvorix.com</li>
    <li><svg viewBox="0 0 22 22"><rect x="4" y="4" width="14" height="14" transform="rotate(45 11 11)" fill="var(--green)"/><path d="M11 16l-3-5a3 3 0 1 1 6 0z" fill="#fff"/></svg><span>418 Birchfield Ln.<br>Unit 1 &amp; 2 Oakdale, KY 40299</span></li>
  </ul>
  <div class="footer-band"></div>
</main>
</body>
</html>
```